Ferncrest Dental, LLC business card project

Business card to be designed with current logo.
Dental office- please keep design of card that looks clean and professional.
Please include the following info:
Ferncrest Dental, LLC
Dr. Lorna Pettigrew
2871 Marlowe Street
Bethlehem, PA 18093
610-555-0193
ferncrestdental.office@examplemail.test
Hello everyone-
Reason: Just got back from overseas- will look at all designs and provide feedback. Thank you!
Reason: Polling my friends for the final selection-
thank you to all those that participated- so many talented designers!

```html
<!DOCTYPE html>
<html lang="en">
<head>
<meta charset="utf-8">
<title>Ferncrest Dental — Business Card</title>
<link rel="stylesheet" href="https://fonts.googleapis.com/css2?family=Arimo:wght@400&display=swap">
<style>
  :root {
    --card-bg: #ffffff;
    --brand-green: #5e9f3f;
    --arc-dark: #63a144;
    --arc-light: #c5dd64;
    --name-ink: #454545;
    --contact-ink: #9a9a9a;
  }
  html, body {
    margin: 0;
    padding: 0;
    overflow: hidden;
    background: var(--card-bg);
  }
  .card {
    position: relative;
    width: 1200px;
    height: 686px;
    overflow: hidden;
    background: var(--card-bg);
    font-family: "Arimo", Arial, sans-serif;
  }
  .card__arc {
    position: absolute;
    inset: 0;
    width: 1200px;
    height: 686px;
  }
  .brand {
    position: absolute;
    top: 52px;
    right: 24px;
    display: flex;
    align-items: center;
    gap: 22px;
  }
  .brand__dot {
    width: 30px;
    height: 30px;
    border-radius: 50%;
    background: var(--arc-light);
  }
  .brand__name {
    margin: 0;
    font-size: 66px;
    font-weight: 400;
    line-height: 1;
    color: var(--brand-green);
    letter-spacing: -0.5px;
    white-space: nowrap;
  }
  .holder {
    position: absolute;
    left: 25px;
    top: 334px;
    margin: 0;
    font-size: 50px;
    font-weight: 400;
    line-height: 1;
    color: var(--name-ink);
  }
  .contact {
    position: absolute;
    left: 21px;
    top: 490px;
    margin: 0;
    font-style: normal;
    font-size: 36px;
    line-height: 46px;
    color: var(--contact-ink);
  }
  .contact span {
    display: block;
    white-space: nowrap;
  }
</style>
</head>
<body>
  <div class="card">
    <svg class="card__arc" viewBox="0 0 1050 600" preserveAspectRatio="none" aria-hidden="true">
      <circle cx="1080" cy="800" r="482" fill="var(--arc-dark)"/>
      <circle cx="1082" cy="802" r="454" fill="var(--arc-light)"/>
    </svg>

    <header class="brand">
      <span class="brand__dot" aria-hidden="true"></span>
      <h1 class="brand__name">Ferncrest Dental</h1>
    </header>

    <p class="holder">Dr. Lorna Pettigrew</p>

    <address class="contact">
      <span>2871 Marlowe Street</span>
      <span>Bethlehem, PA 18093</span>
      <span>610-555-0193</span>
      <span>ferncrestdental.office@examplemail.test</span>
    </address>
  </div>
</body>
</html>
```